We need a business card for a company which is just starting up. The company name is Lumencrest Executive Services and we do a variety of things such as: support services for executives/leaders, sales team creation/management/training, and implementation of new programs to enhance a company's culture. The final design should be simple, professional and create a buzz of wanting to learn more. The owner is a woman of power, poise and leadership while she maintains qualities of caring, compassionate and honest. Her clients respect and refer her constantly. The colors are up for negotiation but should capture strength and softness at the same time. Possible colors: chocolate brown, dark pink, periwinkle. See attachment.

Target Market(s)

Medium to Large Businesses

Industry/Entity Type

Leadership

Requirements
Nice to have
• Qr code

```html
<!DOCTYPE html>
<html lang="en">
<head>
<meta charset="UTF-8">
<title>Lumencrest Executive Services – Business Card</title>
<link rel="stylesheet" href="https://fonts.googleapis.com/css2?family=Arimo:wght@400&family=Pinyon+Script&display=swap">
<style>
  :root {
    --page-bg: #e9e5e0;
    --night-navy: #0b0e2a;
    --bead-blue: #28326e;
    --bead-gold: #8a6320;
    --swirl-bronze: #b47a30;
    --band-tan: #c6a383;
    --band-cream: #f4ede5;
    --band-white: #ffffff;
    --ink-brown: #2f2118;
    --name-cream: #f1dcb8;
  }
  * { margin: 0; padding: 0; box-sizing: border-box; }
  html, body {
    width: 1200px;
    height: 800px;
    overflow: hidden;
    background: var(--page-bg);
  }
  .business-card {
    position: absolute;
    left: 40px;
    top: 85px;
    width: 1120px;
    height: 630px;
    overflow: hidden;
    box-shadow: 0 10px 30px rgba(0, 0, 0, 0.35);
  }
  .card-artwork {
    position: absolute;
    inset: 0;
    background:
      radial-gradient(ellipse 30% 60% at 45% 40%, rgba(180, 122, 48, 0.75), transparent 75%),
      radial-gradient(ellipse 18% 45% at 26% 55%, rgba(138, 99, 32, 0.7), transparent 75%),
      radial-gradient(ellipse 18% 45% at 84% 40%, rgba(138, 99, 32, 0.7), transparent 75%),
      radial-gradient(ellipse 14% 35% at 6% 70%, rgba(138, 99, 32, 0.55), transparent 75%),
      radial-gradient(ellipse 20% 30% at 62% 90%, rgba(138, 99, 32, 0.55), transparent 75%),
      linear-gradient(160deg, var(--bead-blue), var(--night-navy) 55%, var(--bead-blue));
  }
  .company-name {
    position: absolute;
    left: 60px;
    top: 48px;
    font-family: "Arimo", Arial, sans-serif;
    font-size: 38px;
    line-height: 44px;
    color: var(--name-cream);
  }
  .contact-band {
    position: absolute;
    left: 355px;
    top: 331px;
    right: 0;
    height: 175px;
    border-radius: 30px 0 0 30px;
    background: linear-gradient(90deg, var(--band-tan) 0%, var(--band-cream) 45%, var(--band-white) 100%);
    color: var(--ink-brown);
  }
  .contact-list {
    position: absolute;
    left: 18px;
    top: 18px;
    list-style: none;
    font-family: "Arimo", Arial, sans-serif;
    font-size: 37px;
    line-height: 46px;
  }
  .contact-item {
    display: flex;
    align-items: center;
    gap: 14px;
  }
  .contact-icon {
    width: 34px;
    height: 34px;
    flex: none;
  }
  .owner-block {
    position: absolute;
    right: 22px;
    top: 36px;
    text-align: right;
  }
  .owner-name {
    font-family: "Pinyon Script", cursive;
    font-size: 50px;
    line-height: 50px;
  }
  .owner-title {
    font-family: "Arimo", Arial, sans-serif;
    font-size: 36px;
    line-height: 46px;
  }
</style>
</head>
<body>
  <div class="business-card">
    <div class="card-artwork" role="img" aria-label="Navy and gold beaded texture with flowing bronze ornamental swirls"></div>

    <p class="company-name">Lumencrest Executive Services</p>

    <div class="contact-band">
      <ul class="contact-list">
        <li class="contact-item">
          <svg class="contact-icon" viewBox="0 0 32 32" aria-hidden="true">
            <circle cx="16" cy="16" r="15" fill="var(--ink-brown)"/>
            <path d="M12 8 h4 v5 h-3 v6 h3 v5 h-4 a3 3 0 0 1 -3 -3 v-10 a3 3 0 0 1 3 -3z" fill="#fff"/>
          </svg>
          <span>(555) 555-5555</span>
        </li>
        <li class="contact-item">
          <svg class="contact-icon" viewBox="0 0 32 32" aria-hidden="true">
            <path d="M4 26 C6 16 12 13 19 13 V7 L29 15 L19 23 V18 C12 18 8 20 4 26z" fill="var(--ink-brown)"/>
          </svg>
          <span>www.website.com</span>
        </li>
        <li class="contact-item">
          <svg class="contact-icon" viewBox="0 0 32 32" aria-hidden="true">
            <rect x="3" y="7" width="26" height="18" fill="none" stroke="var(--ink-brown)" stroke-width="2.5"/>
            <path d="M3 7 L16 18 L29 7" fill="none" stroke="var(--ink-brown)" stroke-width="2.5"/>
          </svg>
          <span>marisa@email.com</span>
        </li>
      </ul>

      <div class="owner-block">
        <p class="owner-name">Marisa Calloway</p>
        <p class="owner-title">Owner</p>
      </div>
    </div>
  </div>
</body>
</html>
```